Wordpress theme customised please - for new ecommerce homewares website

Hi, we need a wordpress theme customised for a business that will sell tea towels (aka kitchen towels/dish cloths).
We do not have a website currently, but wish to launch using wordpress + woocommerce + "the marrowfen" theme (c/- getplumwick).
BACKGROUND RE THE BUSINESS
Our products are very stylish and will appeal to people who like owning gorgeous things - people who love cooking and/or decorating their home beautifully, or maybe they like travelling and/or buying presents for themselves and friends/family etc.
As they are typically used in people's kitchens, so "fresh" and "clean" is important - however the site must look very upmarket: timeless yet current, and classic yet simple, but not pretty, fussy or edgy.
We believe we have a great opportunity to leverage the "feel" of the product - cotton & linen fabric that has real texture to it, is tactile, natural, raw, real... in the photos used on the website, the backgrounds etc
Our logo is attached - a very dark grey colour was chosen, with white stripes, so that its neutral colouring would coordinate well with our suppliers' existing packaging. (We will represent a number of brands.)
BACKGROUND RE THIS PROJECT
We already know we want to use "the marrowfen" theme by getplumwick, but we need help customising the look of this theme so it works well with our logo, looks really striking and doesn't look like everyone else's ie "straight out of the box".
It appears these are the types of things that can be changed:
LAYOUT:
home page design concept (eg with a kestrel carousel)
page design concept for eg About Us, Contact Us, FAQs
landing page design concept
header; light footer; dark footer
COLOURS & BACKGROUNDS & BORDERS & SEPARATORS:
main theme colour; accent colour; primary font colour
header background; light footer background colour; dark footer background colour; copyright bar background colour
dark footer widget title border; dark footer list separators and borders; dark footer/copyright bar separator styles
FONTS:
main navigation text colour; secondary navigation text colour; dark footer text colour; copyright bar text colour
main font; secondary font
LASTLY
Please don't hesitate to ask questions, request further information etc This is the first time we've posted a design project like this so it's tricky to know what other information you will need, so please just get in touch, ok!
Thanks so much for your interest in this project, and best wishes.

```html
<!DOCTYPE html>
<html lang="en">
<head>
<meta charset="utf-8">
<title>Dishcloth Drawer — Home</title>
<link rel="stylesheet" href="https://fonts.googleapis.com/css2?family=Libre+Baskerville&family=Oswald:wght@400;500&family=Parisienne&family=Merriweather:wght@900&family=Roboto:wght@400;700;900&family=Lato:wght@400;700&display=swap">
<style>
:root{
  --sky:#00b2f0;
  --sky-deep:#0a86d8;
  --page:#6cb7dd;
  --page-light:#8ccbe9;
  --ink:#262b36;
  --white:#ffffff;
  --card:#f1f1f1;
  --card-line:#dcdcdc;
  --price:#e8141c;
  --muted:#666;
  --green:#8cc63f;
  --gold:#f2b705;
}
*{box-sizing:border-box;margin:0;padding:0}
html,body{width:888px;height:1200px;overflow:hidden}
body{position:relative;font-family:"Lato",sans-serif;color:var(--ink);
  background:radial-gradient(circle at 50% 20%,var(--page-light),var(--page) 70%)}
.abs{position:absolute}

.topbar{left:0;top:0;width:888px;height:34px;background:var(--sky)}
.social{left:38px;top:9px;display:flex;gap:11px}
.social span{width:12px;height:12px;border-radius:50%;background:var(--white)}
.utility{right:56px;top:11px;font-size:8.5px;color:var(--white);letter-spacing:.1px;display:flex;gap:8px}
.search{right:9px;top:0;width:36px;height:34px;border-left:1px solid #0a8ec4;border-right:1px solid #0a8ec4}

.header{left:24px;top:34px;width:835px;height:99px;background:var(--ink)}
.brand{left:12px;top:46px;font-family:"Libre Baskerville",serif;font-size:25px;color:var(--white);letter-spacing:.5px}
.cart{left:726px;top:18px;width:48px;height:15px;border:1px solid var(--gold);color:var(--gold);font:700 7.5px "Lato",sans-serif;text-align:center;line-height:13px}
.cart-bag{left:778px;top:13px;width:18px;height:18px;background:var(--gold);border-radius:2px}
.nav{right:27px;top:61px;display:flex;gap:14px;font-size:10.5px;color:var(--white)}
.nav i{font-style:normal;color:#aaa}

.slider{left:34px;top:150px;width:817px;height:332px;background:var(--sky);border-radius:3px;box-shadow:0 2px 4px rgba(0,0,0,.25)}
.slide{left:5px;top:5px;width:807px;height:322px;background:var(--white)}
.slide-photo{left:4px;top:26px;width:340px;height:240px;border-radius:6px;
  background:linear-gradient(160deg,#e84a4a 0%,#f08a3a 30%,#3aa0e0 55%,#dfeef6 80%,#ffffff 100%);opacity:.85}
.slide-title{left:412px;top:68px;font-family:"Parisienne",cursive;font-size:44px;line-height:54px;color:var(--sky)}
.cta{left:408px;top:198px;width:200px;height:48px;border-radius:24px;background:linear-gradient(var(--sky),var(--sky-deep));
  color:var(--white);font:900 22px "Merriweather",serif;text-align:center;line-height:48px;box-shadow:0 2px 3px rgba(0,0,0,.3)}
.arrow{top:297px}
.dots{left:381px;top:462px;width:120px;height:28px;background:var(--sky);border-radius:8px 8px 0 0;display:flex;gap:3px;justify-content:center;align-items:center}
.dots span{width:10px;height:10px;border-radius:50%;background:#404040}
.dots span:first-child{background:#9acd32}

.content{left:24px;top:501px;width:835px;height:699px;background:var(--white)}
.shipping{left:0;top:0;width:835px;height:104px;background:linear-gradient(#eee,#fff 25%,#fff 75%,#eee)}
.shipping p{position:absolute;left:128px;top:38px;font:700 20px "Roboto",sans-serif;letter-spacing:.3px;color:var(--ink)}
.badge{left:641px;top:12px;width:100px;height:100px;border-radius:50%;background:var(--white);box-shadow:0 3px 6px rgba(0,0,0,.35)}
.badge div{position:absolute;left:7px;top:7px;width:86px;height:86px;border-radius:50%;background:var(--sky);
  font-size:10.5px;line-height:13px;text-align:center;padding-top:24px;color:var(--ink)}

.section-title{left:10px;font:500 19px "Oswald",sans-serif;color:var(--ink)}
.rule{left:10px;width:815px;height:5px;background:var(--sky)}
.rule::before{content:"";position:absolute;left:0;top:0;width:160px;height:5px;background:#3a3a3a}
.pager{right:10px;display:flex;gap:4px}
.pager span{width:21px;height:21px;background:var(--green);color:var(--white);font-size:14px;text-align:center;line-height:20px}

.card{width:193px;height:216px;background:var(--card);border:1px solid var(--card-line)}
.card h3{position:absolute;top:13px;width:100%;text-align:center;font:400 16px "Lato",sans-serif;letter-spacing:.3px}
.card .photo{position:absolute;left:17px;top:40px;width:158px;height:128px}
.card .model{position:absolute;left:27px;top:182px;font-size:8.5px;color:var(--muted)}
.card .price{position:absolute;left:27px;top:194px;font-size:9px;color:var(--price);font-weight:700}
.card .buy{position:absolute;left:111px;top:182px;width:60px;height:22px;border-radius:3px;background:linear-gradient(var(--sky),var(--sky-deep));
  color:var(--white);font-size:8.5px;text-align:center;line-height:22px}
</style>
</head>
<body>
<div class="abs topbar"></div>
<div class="abs social"><span></span><span></span><span></span><span></span><span></span><span></span><span></span><span></span></div>
<div class="abs utility"><span>TRACK YOUR ORDER</span><span>|</span><span>MY ACCOUNT</span><span>|</span><span>REGISTER</span></div>
<div class="abs search"><svg width="36" height="34" viewBox="0 0 36 34"><circle cx="16" cy="15" r="5" fill="none" stroke="#23464f" stroke-width="2"/><line x1="20" y1="19" x2="24" y2="23" stroke="#23464f" stroke-width="2.5"/></svg></div>

<header class="abs header">
  <div class="abs brand">DISHCLOTH DRAWER</div>
  <div class="abs cart">0 ITEMS</div>
  <div class="abs cart-bag"></div>
  <nav class="abs nav"><span>HOME</span><i>|</i><span>ABOUT</span><i>|</i><span>SERVICES</span><i>|</i><span>PRODUCTS</span><i>|</i><span>BLOG</span><i>|</i><span>CONTACT</span></nav>
</header>

<section class="abs slider">
  <div class="abs slide">
    <div class="abs slide-photo" role="img" aria-label="Stack of folded striped tea towels beside a blue napkin in a cup"></div>
    <div class="abs slide-title">Aka Kitchen Towels,<br>Dish Clothes</div>
    <div class="abs cta">Know More</div>
  </div>
</section>
<svg class="abs arrow" style="left:24px" width="42" height="48" viewBox="0 0 42 48"><rect width="42" height="44" rx="4" fill="#1a8fd6"/><path d="M27 12 L13 22 L27 32Z" fill="#0b3d66"/></svg>
<svg class="abs arrow" style="left:818px" width="42" height="48" viewBox="0 0 42 48"><rect width="42" height="44" rx="4" fill="#1a8fd6"/><path d="M15 12 L29 22 L15 32Z" fill="#0b3d66"/></svg>
<div class="abs dots"><span></span><span></span><span></span><span></span><span></span></div>

<main class="abs content">
  <div class="abs shipping"><p>FREE SHIPPING ON ALL ORDERS OVER $50.00</p></div>
  <div class="abs badge"><div>Deliver to<br>your doors on<br>3 days</div></div>

  <h2 class="abs section-title" style="top:127px">FEATURED PRODUCTS</h2>
  <div class="abs pager" style="top:140px"><span>‹</span><span>›</span></div>
  <div class="abs rule" style="top:165px"></div>

  <div class="abs card" style="left:10px;top:184px"><h3>Towel 1</h3><div class="photo" role="img" aria-label="Blue patterned hanging towel with button" style="background:linear-gradient(#6fb8d8,#5a5050)"></div><span class="model">MODEL 12458</span><span class="price">$25.69</span><span class="buy">BUY NOW</span></div>
  <div class="abs card" style="left:218px;top:184px"><h3>Towel 2</h3><div class="photo" role="img" aria-label="White waffle towel on a hook" style="background:linear-gradient(#e8e2de,#d8cfc8)"></div><span class="model">MODEL 12458</span><span class="price">$25.69</span><span class="buy">BUY NOW</span></div>
  <div class="abs card" style="left:425px;top:184px"><h3>Dish Clothes 1</h3><div class="photo" role="img" aria-label="Printed linen dish cloths hanging" style="background:linear-gradient(90deg,#2a2a2a,#c9b8a6 55%,#d8cbbb)"></div><span class="model">MODEL 12458</span><span class="price">$25.69</span><span class="buy">BUY NOW</span></div>
  <div class="abs card" style="left:633px;top:184px"><h3>Dish Clothes 2</h3><div class="photo" role="img" aria-label="Linen cloth with teal seahorse print" style="background:linear-gradient(#e4ddd2,#d4cbbd)"></div><span class="model">MODEL 12458</span><span class="price">$25.69</span><span class="buy">BUY NOW</span></div>

  <h2 class="abs section-title" style="top:423px">BEST SELLERS</h2>
  <div class="abs pager" style="top:436px"><span>‹</span><span>›</span></div>
  <div class="abs rule" style="top:461px"></div>

  <div class="abs card" style="left:10px;top:480px"><h3>Towel 1</h3><div class="photo" role="img" aria-label="White waffle towel on a hook" style="background:linear-gradient(#e8e2de,#d8cfc8)"></div><span class="model">MODEL 12458</span><span class="price">$25.69</span><span class="buy">BUY NOW</span></div>
  <div class="abs card" style="left:218px;top:480px"><h3>Towel 2</h3><div class="photo" role="img" aria-label="Folded white towel tied with a ruffled fabric band" style="background:linear-gradient(#3a2a22,#f0efe8 30%,#f0efe8 70%,#3a2a22)"></div><span class="model">MODEL 12458</span><span class="price">$25.69</span><span class="buy">BUY NOW</span></div>
  <div class="abs card" style="left:425px;top:480px"><h3>Dish Clothes 1</h3><div class="photo" role="img" aria-label="Printed linen dish cloths hanging" style="background:linear-gradient(90deg,#2a2a2a,#c9b8a6 55%,#d8cbbb)"></div><span class="model">MODEL 12458</span><span class="price">$25.69</span><span class="buy">BUY NOW</span></div>
  <div class="abs card" style="left:633px;top:480px"><h3>Dish Clothes 2</h3><div class="photo" role="img" aria-label="Blue check cloth with a knife and herbs" style="background:linear-gradient(#dfe9f4,#b8cde6)"></div><span class="model">MODEL 12458</span><span class="price">$25.69</span><span class="buy">BUY NOW</span></div>
</main>
</body>
</html>
```